Re-Brand of TindelMox along with a new website design

TindelMox Ltd are a software & database development company using technologies such as PHP, C#, HTML, JQuery, Flex, AS3, MySQL, Oracle, MSSQL. We like to target all types of business from small to large.

We are great at coding but rubbish at design so thats where we need your help!

We want a complete re-brand of TindelMox including logo, website design, and business cards.

We would like a design that is clean but other than that, please feel free to be creative.

****Logo****
We are looking for a logo that appears professional but with a splash of colour that indicates a creative side. Please see below some logos that we like the look of:

We like this one because it has a nice simple and clear font for the name of the company but also an icon which is colourful and stands out. http://markvault.example/2013/03/brivelo/

We like this one because it is very clean, simple and again very clear. http://markvault.example/2013/03/quantorels/

http://markvault.example/2013/03/tide-lamp/
http://markvault.example/2013/02/velmorin/
http://markvault.example/2013/01/art-gallery-tarnwick/

As you will see from all of these examples, the font is very clear but there is always a graphic representing the company too. This is what we like.

****Website****
These are some of the examples of websites we like:
https://www.zestrune.example/
https://www.chatterlane.example/home
http://www.haldenimagery.example/
http://www.vistor.example/
http://quillbay.example/
https://www.usebriefnest.example/personal-intros
http://www.marmotpanel.example/

The current site can be found at tindelmox.example.uk

Reason: We have extended the deadline of the project by 5 days as I realise the original deadline was very tight.

Software

Requirements
Must have
• Website must have the following pages
Home
Services
Projects
About Us
Contact Us

```html
<!DOCTYPE html>
<html lang="en">
<head>
<meta charset="utf-8">
<title>TindelMox – Home</title>
<link href="https://fonts.googleapis.com/css2?family=Advent+Pro:wght@300;400&family=Arimo:wght@400;700&display=swap" rel="stylesheet">
<style>
:root{
  --black:#000;
  --white:#fff;
  --lime:#d6df22;
  --lime-bright:#d9e021;
  --field:#e6e11c;
  --nav-active:#d6df22;
  --dark:#3b3b3c;
  --display:'Advent Pro', sans-serif;
  --text:'Arimo', Arial, sans-serif;
}
*{margin:0;padding:0;box-sizing:border-box}
html,body{width:1020px;height:1200px;overflow:hidden;background:var(--black)}
.page{position:relative;width:1020px;height:1200px;font-family:var(--text);color:var(--white)}
.site-header{position:absolute;left:0;top:0;width:1020px;height:118px;background:var(--black)}
.brand{position:absolute;left:24px;top:36px;display:flex;align-items:center;gap:14px}
.brand-mark{width:40px;height:40px;background:var(--lime)}
.brand-name{font-family:var(--display);font-weight:300;font-size:46px;line-height:1;color:var(--white)}
.main-nav{position:absolute;top:40px;right:43px;display:flex;gap:0}
.main-nav a{font-family:var(--display);font-weight:300;font-size:33px;color:var(--white);text-decoration:none;line-height:44px}
.main-nav a.is-active{color:var(--nav-active)}
.main-nav a+a{margin-left:42px}
.header-rule{position:absolute;left:0;top:118px;width:1020px;height:6px;background:var(--white)}
.hero{position:absolute;left:0;top:124px;width:1020px;height:470px;
  background:linear-gradient(100deg,#8fb8d8 0%,#a9cbe3 30%,#b7c3bb 55%,#8b9a92 80%,#6f7a74 100%)}
.hero-title{position:absolute;right:45px;top:226px;text-align:right;font-family:var(--display);color:var(--white);line-height:56px}
.hero-title .light{display:block;font-weight:300;font-size:56px}
.hero-title .strong{display:block;font-weight:400;font-size:56px}
.divider{position:absolute;left:0;top:586px;width:1020px;height:64px}
.intro{position:absolute;left:0;top:650px;width:1020px;height:332px;
  background:linear-gradient(to bottom,#202021 0%,#050505 35%,var(--black) 100%)}
.intro-copy{position:absolute;left:60px;top:18px;width:860px;text-align:center;font-size:21px;line-height:21.5px}
.intro-copy p+p{margin-top:21.5px}
.site-footer{position:absolute;left:0;top:982px;width:1020px;height:218px;background:var(--lime-bright)}
.footer-col{position:absolute;top:18px}
.footer-col h3{font-size:15.5px;font-weight:700;padding-left:4px;padding-bottom:2px;border-bottom:1.5px solid var(--white);line-height:18px}
.footer-col ul{list-style:none;margin-top:11px;padding-left:2px;font-size:13px;line-height:17px}
.contact{left:65px;width:195px}
.contact dl{margin-top:12px;padding-left:2px;font-size:13px;line-height:13.5px}
.contact dd+dt{margin-top:6px}
.services{left:303px;width:195px}
.social{left:520px;width:178px}
.social-icons{display:flex;margin-top:5px}
.social-icons span{width:29px;height:29px;border-radius:50%;background:#2b9bd8;margin-right:0}
.social-icons span:nth-child(3){background:#e04a4a}
.social-icons span:nth-child(4){background:#f2a43b}
.newsletter{left:735px;width:200px}
.newsletter h3{font-weight:400;border:none;padding-left:0}
.email-field{position:absolute;left:730px;top:1035px;width:195px;height:30px;background:var(--field);border:none;box-shadow:inset 0 1px 3px rgba(0,0,0,.35);font-size:9px;color:#9a9a20;padding:9px 8px}
.submit-btn{position:absolute;left:855px;top:1080px;width:67px;height:27px;border-radius:3px;background:linear-gradient(#555,#111);color:var(--white);font-size:13px;text-align:center;line-height:27px;box-shadow:0 2px 3px rgba(0,0,0,.4)}
</style>
</head>
<body>
<div class="page">
  <header class="site-header">
    <div class="brand"><span class="brand-mark"></span><span class="brand-name">TindelMox</span></div>
    <nav class="main-nav">
      <a class="is-active" href="#">Home</a>
      <a href="#">Services</a>
      <a href="#">Projects</a>
      <a href="#">About Us</a>
      <a href="#">Contact Us</a>
    </nav>
  </header>
  <div class="header-rule"></div>

  <section class="hero" role="img" aria-label="Photo of a smiling man in a light blue shirt using a tablet">
  </section>
  <h1 class="hero-title"><span class="light">TindelMox is the right</span><span class="strong">team for you</span></h1>

  <svg class="divider" width="1020" height="64" viewBox="0 0 1020 64" aria-hidden="true">
    <defs><linearGradient id="dividerShade" x1="0" y1="0" x2="0" y2="1"><stop offset="0" stop-color="#3b3b3c"/><stop offset="1" stop-color="#202021"/></linearGradient></defs>
    <polygon points="0,2 402,2 510,40 618,2 1020,2 1020,16 618,16 510,54 402,16 0,16" fill="#d6df22"/>
    <polygon points="0,16 402,16 510,54 618,16 1020,16 1020,64 0,64" fill="url(#dividerShade)"/>
  </svg>

  <section class="intro">
    <div class="intro-copy">
      <p>if you are looking for web, software, or IT services that really deliver but you don't want to pay over the odds then TindelMox is the right team for you.</p>
      <p>Based in Brantham Vale our clients are both local, national, both large and small. You may be a start-up business in need of a 'get me up and running quickly' website, or a multi-million pound brand looking for an all singing, all dancing bespoke app.</p>
      <p>Maybe you are experiencing the pains and pleasures of growing your business and its time to improve your branding and to trade in your current home spun website for something more professional.</p>
      <p>Let's chat today about where we can take your business.</p>
    </div>
  </section>

  <footer class="site-footer">
    <div class="footer-col contact">
      <h3>CONTACT US</h3>
      <dl>
        <dt>Telephone</dt><dd>01632 960 418</dd>
        <dt>Email</dt><dd>contact@tindelmox.example.uk</dd>
        <dt>Address</dt><dd>42 Corvell Lane<br>Brantham Vale<br>Wendmoor<br>BV4 7QT</dd>
      </dl>
    </div>
    <div class="footer-col services">
      <h3>SERVICES</h3>
      <ul>
        <li>Website Design &amp; Development</li>
        <li>Rich Internet Applications</li>
        <li>Mobile &amp; Tablet Applications</li>
        <li>Mobile &amp; Tablet Applications</li>
        <li>Database Development</li>
        <li>Database Reporting</li>
        <li>Games</li>
        <li>IT Services</li>
        <li>IT Security</li>
      </ul>
    </div>
    <div class="footer-col social">
      <h3>SOCIAL NETWORKS</h3>
      <div class="social-icons"><span></span><span></span><span></span><span></span></div>
    </div>
    <div class="footer-col newsletter">
      <h3>NEWSLETTER SIGNUP</h3>
    </div>
  </footer>
  <div class="email-field">Enter your email here</div>
  <div class="submit-btn">SUBMIT</div>
</div>
</body>
</html>
```